Startup company business card (Media & Advertising)

we need a business card design for a company that is a startup in the media and aggregation industry. Card needs to look funky and of a new breed/modern and upmarket.

Target Market(s)

advertisers/ brand agencies & media publishers

Industry/Entity Type

Advertising

Contact Information for Business Card

Please ensure the front face signifies our brand (plintovo.com) and back has details for the contact. Standard contact such as phone , address, email , website etc.

Font styles to use
Other font styles liked:
• use styleguide and logo font and color

Colors

Designer to choose colors to be used in the design.

Requirements
Must have
• We are disrupting the media and agency industry so subtlety would be good to use imagery to signify this
Nice to have
• Please use logo colors for branding
Should not have
• be as creative and provide few options. Pick a brand color from logo and styleguide

```html
<!DOCTYPE html>
<html lang="en">
<head>
<meta charset="utf-8">
<title>plintovo business card</title>
<link rel="stylesheet" href="https://fonts.googleapis.com/css2?family=Archivo+Black&family=Arimo:wght@400&family=Open+Sans:wght@400;600&display=swap">
<style>
  :root {
    --bg: #ecebe8;
    --card: #ffffff;
    --brand-red: #ef3e4a;
    --brand-red-soft: #f26a72;
    --ink: #141414;
    --navy: #1f2a6b;
    --teal: #1d7f8c;
    --shadow: rgba(0, 0, 0, 0.18);
  }
  * { box-sizing: border-box; margin: 0; padding: 0; }
  html, body { width: 1200px; height: 900px; overflow: hidden; background: var(--bg); }
  .canvas { position: relative; width: 1200px; height: 900px; }
  .card {
    position: absolute; left: 300px; width: 600px; height: 343px;
    background: var(--card); box-shadow: 0 10px 28px var(--shadow);
    overflow: hidden;
  }
  .card--front { top: 70px; }
  .card--back { top: 487px; }

  .wordmark {
    position: absolute; display: flex; align-items: center; gap: 10px;
    font-family: "Archivo Black", sans-serif; color: var(--ink); letter-spacing: 0.5px;
  }
  .wordmark__dot { border-radius: 50%; background: var(--brand-red); }
  .card--front .wordmark { left: 48px; top: 52px; font-size: 22px; }
  .card--front .wordmark__dot { width: 20px; height: 20px; }
  .card--back .wordmark { left: 150px; top: 66px; font-size: 34px; }
  .card--back .wordmark__dot { width: 30px; height: 30px; }

  .name-pill {
    position: absolute; left: 318px; top: 208px; width: 250px; height: 58px;
    border-radius: 29px; background: var(--brand-red);
    display: flex; flex-direction: column; justify-content: center; padding-left: 44px;
    font-family: "Open Sans", sans-serif; line-height: 1.15;
  }
  .name-pill__name { color: #fff; font-size: 17px; }
  .name-pill__role { color: var(--ink); font-size: 17px; }

  .divider { position: absolute; left: 0; right: 0; top: 150px; height: 3px; background: var(--brand-red); }

  .brand-flock {
    position: absolute; left: 360px; top: 112px; width: 220px; height: 80px;
    border-radius: 8px;
    background: linear-gradient(135deg, var(--brand-red-soft), var(--brand-red));
    opacity: 0.85;
  }

  .contact { position: absolute; list-style: none; font-family: "Arimo", sans-serif; color: var(--navy); font-size: 15px; }
  .contact li { display: flex; align-items: center; gap: 10px; height: 26px; letter-spacing: 0.6px; }
  .contact--left { left: 28px; top: 172px; }
  .contact--right { left: 290px; top: 238px; }
  .contact--right li { word-spacing: 6px; }
  .icon { width: 22px; height: 22px; flex: none; }
</style>
</head>
<body>
<main class="canvas">

  <section class="card card--front" aria-label="Card front">
    <div class="wordmark"><span class="wordmark__dot"></span>plintovo</div>
    <div class="name-pill">
      <span class="name-pill__name">Dara Welling</span>
      <span class="name-pill__role">Founder&amp;CEO</span>
    </div>
  </section>

  <section class="card card--back" aria-label="Card back">
    <div class="wordmark"><span class="wordmark__dot"></span>plintovo</div>
    <div class="divider"></div>
    <div class="brand-flock" role="img" aria-label="Flock of brand marks in red"></div>

    <ul class="contact contact--left">
      <li>
        <svg class="icon" viewBox="0 0 22 22"><circle cx="11" cy="11" r="10" fill="none" stroke="var(--teal)" stroke-width="2"/><path d="M6 9 Q11 5 16 9 L14.5 10.5 L13 9.5 L9 9.5 L7.5 10.5 Z M8 11 H14 L15 15 H7 Z" fill="var(--teal)"/></svg>
        + 00-000-0000
      </li>
      <li>
        <svg class="icon" viewBox="0 0 22 22"><circle cx="11" cy="11" r="10" fill="none" stroke="var(--teal)" stroke-width="2"/><rect x="5.5" y="7" width="11" height="8" fill="var(--teal)"/><path d="M5.5 7 L11 11.5 L16.5 7" fill="none" stroke="#fff" stroke-width="1.2"/></svg>
        info@yourdomain.com
      </li>
    </ul>

    <ul class="contact contact--right">
      <li>
        <svg class="icon" viewBox="0 0 22 22"><circle cx="11" cy="11" r="10" fill="none" stroke="var(--teal)" stroke-width="2"/><circle cx="11" cy="11" r="6" fill="none" stroke="var(--teal)" stroke-width="1.6"/><path d="M5 11 H17 M11 5 V17" stroke="var(--teal)" stroke-width="1.4"/></svg>
        www.plintovo.com
      </li>
      <li>
        <svg class="icon" viewBox="0 0 22 22"><circle cx="11" cy="11" r="10" fill="none" stroke="var(--teal)" stroke-width="2"/><path d="M5 11.5 L11 6 L17 11.5 H15 V16 H7 V11.5 Z" fill="var(--teal)"/></svg>
        Your Countrey Name
      </li>
    </ul>
  </section>

</main>
</body>
</html>
```